Brisk Harbor
Where Your Harbor Counts
Brisk Harbor - Consulting
Creative Brief
Professional
Marlo Fenwick
4817 Tulip Meadow Lane San Diego, CA 92143
briskharbor1@plumetide.com
I would like to have my logo on one side and see a monogram on the front, but all designs are welcome, thanks.

```html
<!DOCTYPE html>
<html lang="en">
<head>
<meta charset="utf-8">
<title>Brisk Harbor – Business Card</title>
<link rel="stylesheet" href="https://fonts.googleapis.com/css2?family=Cormorant+SC:wght@500;600&family=Open+Sans:wght@700&display=swap">
<style>
  :root {
    --brand-blue: #0f4c99;
    --brand-blue-deep: #0a3d80;
    --brand-blue-light: #1c64b6;
    --brand-orange: #ec8424;
    --brand-orange-light: #f4a035;
    --paper: #ffffff;
    --canvas: #ffffff;
    --frame: #8c8c8c;
  }
  * { box-sizing: border-box; margin: 0; padding: 0; }
  html, body {
    width: 1200px;
    height: 725px;
    overflow: hidden;
    background: var(--canvas);
  }
  .sheet {
    position: relative;
    width: 1200px;
    height: 725px;
  }
  .card {
    position: absolute;
    width: 564px;
    height: 326px;
    overflow: hidden;
  }
  .card--front { left: 24px; top: 29px; background: var(--paper); border: 1px solid var(--frame); }
  .card--back-blue { left: 612px; top: 29px; background: linear-gradient(135deg, var(--brand-blue-light), var(--brand-blue-deep)); }
  .card--back-white { left: 24px; top: 372px; background: var(--paper); border: 1px solid var(--frame); }
  .card--back-orange { left: 612px; top: 372px; background: linear-gradient(135deg, var(--brand-orange-light), var(--brand-orange)); }

  .wave {
    position: absolute;
    inset: 0;
    width: 100%;
    height: 100%;
  }

  .brand {
    position: absolute;
    display: flex;
    align-items: center;
    gap: 10px;
    font-family: "Open Sans", Arial, sans-serif;
    font-weight: 700;
    letter-spacing: 0.5px;
    text-transform: uppercase;
    white-space: nowrap;
  }
  .brand__dot {
    display: block;
    border-radius: 50%;
    background: var(--brand-orange);
  }
  .brand--corner {
    left: 20px;
    top: 62px;
    font-size: 25px;
    color: var(--brand-blue);
  }
  .brand--corner .brand__dot { width: 14px; height: 14px; }

  .brand--center {
    left: 50%;
    top: 50%;
    transform: translate(-50%, -50%);
    font-size: 44px;
    gap: 14px;
  }
  .brand--center .brand__dot { width: 20px; height: 20px; }
  .brand--on-color { color: var(--paper); }
  .brand--on-color .brand__dot { background: var(--paper); }
  .brand--on-white { color: var(--brand-blue); }

  .holder-name {
    position: absolute;
    left: 178px;
    top: 116px;
    font-family: "Cormorant SC", Georgia, serif;
    font-weight: 500;
    font-size: 27px;
    color: var(--brand-blue);
  }

  .contact {
    position: absolute;
    left: 20px;
    top: 240px;
    font-family: "Cormorant SC", Georgia, serif;
    font-weight: 600;
    font-size: 15px;
    line-height: 19px;
    color: var(--paper);
    font-style: normal;
  }
</style>
</head>
<body>
<main class="sheet">

  <section class="card card--front" aria-label="Card front">
    <svg class="wave" viewBox="0 0 564 326" preserveAspectRatio="none" aria-hidden="true">
      <defs>
        <linearGradient id="waveBlue" x1="0" y1="0" x2="1" y2="1">
          <stop offset="0" stop-color="#1c64b6"/>
          <stop offset="1" stop-color="#0a3d80"/>
        </linearGradient>
      </defs>
      <path d="M0 165 C150 212 390 262 564 168 L564 326 L0 326 Z" fill="var(--brand-orange)"/>
      <path d="M0 172 C150 219 392 270 564 178 L564 326 L0 326 Z" fill="url(#waveBlue)"/>
    </svg>

    <div class="brand brand--corner">
      <span class="brand__dot"></span>
      <span class="brand__name">Brisk Harbor</span>
    </div>

    <h1 class="holder-name">Marlo Fenwick</h1>

    <address class="contact">
      4817 Tulip Meadow Lane<br>
      San Diego, CA 92143<br>
      Email: briskharbor1@plumetide.com
    </address>
  </section>

  <section class="card card--back-blue" aria-label="Card back, blue">
    <div class="brand brand--center brand--on-color">
      <span class="brand__dot"></span>
      <span class="brand__name">Brisk Harbor</span>
    </div>
  </section>

  <section class="card card--back-white" aria-label="Card back, white">
    <div class="brand brand--center brand--on-white">
      <span class="brand__dot"></span>
      <span class="brand__name">Brisk Harbor</span>
    </div>
  </section>

  <section class="card card--back-orange" aria-label="Card back, orange">
    <div class="brand brand--center brand--on-color">
      <span class="brand__dot"></span>
      <span class="brand__name">Brisk Harbor</span>
    </div>
  </section>

</main>
</body>
</html>
```